Einladungskarten für Der Helle Bogen
Designer hat mehrere Vorschläge entwickelt und Änderungen super schnell umgesetzt. Wir waren sehr zufrieden und freuen uns auf unsere diesjährige Einladungskarte.
Zielgruppe
Wir sind ein Tochterunternehmen von Harting Verlag. Wir sind 'Der Helle Bogen' , Holding der Radio Stationen/Beteiligungen und möchten alle Geschäftsführer/innen der Beteiligungen, einige Politiker und Medienräte zu einem Event einladen.
Aufgabenstellung
Wir hätten gerne eine quadratische Karte.
Das Event heißt 'Ortsabend 2023'
Termin 03.07.2023 um 19 Uhr
Anmeldung bis spätestens 23.06.2022 an events@heller-bogen.de
Diese Karte gilt als Eintrittskarte
Adresse: KAIHALLE, Lindenweg 52, 90461 Nürnberg
Dresscode: Business Casual
Firmenfarben: Blau: RGB 23/110/182 und Grau: RGB 134/135/135
Firmenschriftart: Century Gothic

```html
<!DOCTYPE html>
<html lang="de">
<head>
<meta charset="utf-8">
<title>Ortsabend 2023 – Einladung</title>
<link href="https://fonts.googleapis.com/css2?family=Questrial&family=Mulish:wght@700;800&family=Rubik:wght@800&display=swap" rel="stylesheet">
<style>
  :root {
    --blue: rgb(23,110,182);
    --grey: rgb(134,135,135);
    --paper: #ffffff;
    --stage: #ececec;
    --sky: #b9cbe0;
    --lake: #8fa6a3;
    --green: #6f8a4a;
    --deck: #7a6a58;
  }
  * { box-sizing: border-box; margin: 0; padding: 0; }
  html, body { width: 1200px; height: 1200px; overflow: hidden; }
  body {
    background: var(--stage);
    font-family: 'Questrial', 'Century Gothic', sans-serif;
    color: var(--grey);
    position: relative;
  }
  .card {
    position: absolute;
    top: 330px;
    width: 540px;
    height: 540px;
    background: var(--paper);
    box-shadow: 0 12px 28px rgba(0,0,0,.18);
    overflow: hidden;
  }
  .card--front { left: 40px; }
  .card--back { left: 620px; }

  /* front */
  .front-title {
    position: absolute; left: 80px; top: 38px;
    font-size: 46px; letter-spacing: 1px; color: var(--grey);
    line-height: 1;
  }
  .front-rule {
    position: absolute; left: 80px; top: 95px; width: 382px;
    height: 2px; background: var(--grey);
  }
  .photo {
    position: absolute;
  }
  .photo--terrace {
    left: 0; top: 96px; width: 540px; height: 360px;
    background: linear-gradient(180deg, var(--sky) 0%, #d9d5cc 30%, var(--green) 50%, var(--lake) 62%, var(--deck) 100%);
    z-index: 0;
  }
  .front-title, .front-rule, .brand-mark { z-index: 2; }
  .brand-mark {
    position: absolute; left: 430px; top: 106px;
    width: 26px; height: 26px; background: var(--blue);
  }
  .front-headline {
    position: absolute; left: 92px; top: 188px;
    font-family: 'Rubik', sans-serif; font-weight: 800;
    font-size: 68px; color: #fff;
    transform: rotate(-8deg); transform-origin: left center;
    text-shadow: 0 3px 6px rgba(0,0,0,.35);
    z-index: 2;
  }
  .event-name {
    display: flex; align-items: center; gap: 12px;
    font-size: 42px; line-height: 1; color: var(--blue);
    white-space: nowrap;
  }
  .event-name .dot {
    width: 22px; height: 22px; border-radius: 50%; background: var(--grey);
  }
  .front-footer {
    position: absolute; left: 0; right: 0; top: 456px; height: 84px;
    display: flex; align-items: center; justify-content: center;
  }

  /* back */
  .back-header {
    position: absolute; left: 0; right: 0; top: 0; height: 68px;
    display: flex; align-items: center; justify-content: center;
  }
  .photo--deck {
    left: 0; top: 68px; width: 540px; height: 222px;
    background: linear-gradient(180deg, #dfe3dc 0%, #9fb08b 35%, #b8c6c8 60%, #7d8f6a 100%);
  }
  .dresscode {
    position: absolute; left: 16px; top: 90px;
    font-family: 'Rubik', sans-serif; font-weight: 800;
    font-size: 22px; line-height: 1.15; color: #fff;
    transform: rotate(-5deg); transform-origin: left top;
    text-shadow: 0 2px 4px rgba(0,0,0,.45);
  }
  .play-icon { position: absolute; left: 44px; top: 322px; }
  .details { position: absolute; left: 145px; top: 316px; width: 370px; }
  .date-line { font-size: 21px; color: var(--grey); white-space: nowrap; }
  .date-line strong, .reg strong {
    font-family: 'Mulish', sans-serif; font-weight: 800;
  }
  .date-line strong { color: var(--blue); }
  .timeline { display: block; margin: 12px 0 10px -4px; }
  .reg { font-size: 17px; line-height: 1.45; color: var(--grey); }
  .reg strong { font-weight: 700; }
  .address {
    position: absolute; left: 47px; top: 438px;
    font-size: 14.5px; line-height: 1.3; color: var(--grey);
  }
  .ticket-note {
    position: absolute; right: 30px; top: 490px;
    font-family: 'Mulish', sans-serif; font-weight: 800;
    font-size: 18px; color: var(--blue);
  }
</style>
</head>
<body>

<section class="card card--front">
  <div class="photo photo--terrace" role="img" aria-label="Foto: Seeterrasse mit Sonnenschirm, Holztischen und weißen Stühlen, dahinter See mit Segelbooten"></div>
  <h1 class="front-title">DER HELLE BOGEN</h1>
  <div class="front-rule"></div>
  <div class="brand-mark"></div>
  <p class="front-headline">Einladung</p>
  <footer class="front-footer">
    <div class="event-name">ORTSABEND <span class="dot"></span> <span style="color:var(--grey)">2023</span></div>
  </footer>
</section>

<section class="card card--back">
  <header class="back-header">
    <div class="event-name">ORTSABEND <span class="dot"></span> <span style="color:var(--grey)">2023</span></div>
  </header>
  <div class="photo photo--deck" role="img" aria-label="Foto: Steg mit Glasgeländer und weißen Stühlen am See, umrahmt von Grün und Blumen"></div>
  <p class="dresscode">Dresscode:<br>Business Casual</p>

  <svg class="play-icon" width="66" height="84" viewBox="0 0 66 84" aria-hidden="true">
    <polygon points="3,3 3,81 62,42" fill="none" stroke="var(--blue)" stroke-width="3.5" stroke-linejoin="miter"/>
  </svg>

  <div class="details">
    <p class="date-line">Termin <strong>03.07.2023</strong> um <strong>19 Uhr</strong></p>
    <svg class="timeline" width="370" height="22" viewBox="0 0 370 22" aria-hidden="true">
      <line x1="0" y1="11" x2="350" y2="11" stroke="var(--grey)" stroke-width="2"/>
      <circle cx="355" cy="11" r="9" fill="none" stroke="var(--grey)" stroke-width="2"/>
      <circle cx="355" cy="11" r="5" fill="var(--grey)"/>
    </svg>
    <p class="reg">Anmeldung bis spätestens <strong>23.06.2022</strong><br>an events@heller-bogen.de</p>
  </div>

  <address class="address" style="font-style:normal">
    Adresse:<br>KAIHALLE<br>Lindenweg 52<br>90461 Nürnberg
  </address>
  <p class="ticket-note">Diese Karte gilt als Eintrittskarte</p>
</section>

</body>
</html>
```